Shampoo and Shower Gel Packaging Design

I need a new packaging design for a men shampoo and shower gel bottle. The packaging must me black (black bottle/package) and the logo should be also monochrom.
For example, black matte bottle and black shiny logo on the packaging (not mandatory).
the design must contain maximum 3 colors.
1. black
2. white (text)
3. grey/dark blue/dark green (colors will be the difference between products parfumes/smell/scences.

Design must be minimalist/elegant/discrete.
Updates

Please check the photos i added for pure inspiration.

Target Market(s)

brand exclusively for MEN - premium clients

Industry/Entity Type

Cosmetics

Font styles to use
Sans Serif

Colors
1b1b1b
5c5c5c
aaaaaa
ffffff
3176b5

Requirements
Must have
• black background
• minimalist design

```html
<!DOCTYPE html>
<html lang="en">
<head>
<meta charset="utf-8">
<title>Norvan Cosmetics – Bath &amp; Shower Gel Label</title>
<link rel="stylesheet" href="https://fonts.googleapis.com/css2?family=Josefin+Sans:wght@100;300;400&display=swap">
<style>
  :root {
    --label-black: #1b1b1b;
    --deep-black: #0c0d0f;
    --type-light: #d9d9d9;
    --type-grey: #aaaaaa;
    --accent-blue: #3176b5;
    --accent-grey: #5c5c5c;
  }
  * { margin: 0; padding: 0; box-sizing: border-box; }
  html, body {
    width: 1200px;
    height: 2644px;
    overflow: hidden;
    background: var(--deep-black);
  }
  .label {
    position: relative;
    width: 1200px;
    height: 2644px;
    background: radial-gradient(ellipse at 50% 45%, var(--label-black) 0%, var(--deep-black) 75%);
    font-family: "Josefin Sans", sans-serif;
    font-weight: 300;
    color: var(--type-light);
    text-align: center;
  }
  .brand-dot {
    position: absolute;
    left: 550px;
    top: 1130px;
    width: 100px;
    height: 100px;
    border-radius: 50%;
    border: 3px solid var(--type-light);
  }
  .brand-name {
    position: absolute;
    left: 0;
    width: 1200px;
    top: 1300px;
    font-size: 124px;
    font-weight: 100;
    line-height: 1;
    letter-spacing: 0.52em;
    padding-left: 0.52em;
  }
  .brand-descriptor {
    position: absolute;
    left: 0;
    width: 1200px;
    top: 1440px;
    font-size: 26px;
    color: var(--type-grey);
    letter-spacing: 0.5em;
    padding-left: 0.5em;
  }
  .accent-band {
    position: absolute;
    left: 40px;
    top: 1640px;
    width: 1120px;
    height: 120px;
    border-radius: 60px;
    background: linear-gradient(90deg,
      rgba(49, 118, 181, 0) 0%,
      rgba(49, 118, 181, 0.35) 25%,
      rgba(92, 92, 92, 0.35) 55%,
      rgba(49, 118, 181, 0.35) 80%,
      rgba(49, 118, 181, 0) 100%);
    filter: blur(6px);
  }
  .product-name {
    position: absolute;
    left: 0;
    width: 1200px;
    top: 2296px;
    font-size: 42px;
    font-weight: 300;
    letter-spacing: 0.12em;
  }
  .product-volume {
    position: absolute;
    left: 0;
    width: 1200px;
    top: 2548px;
    font-size: 38px;
    font-weight: 300;
    letter-spacing: 0.04em;
  }
</style>
</head>
<body>
  <main class="label">
    <div class="brand-dot" aria-hidden="true"></div>
    <h1 class="brand-name">NORVAN</h1>
    <p class="brand-descriptor">COSMETICS</p>

    <div class="accent-band" role="img" aria-label="Flowing blue and white wave accent lines"></div>

    <p class="product-name">BATH &amp; SHOWER GEL</p>
    <p class="product-volume">300 ml</p>
  </main>
</body>
</html>
```